WP website design (Holt)

We need a wordpress design for an established auction and real estate company based in Iowa. The winning design will incorporate a professional color scheme with company logo in a clean layout. The design needs to consider that this will be developed on a responsive theme. Colors are those that will highlight the logo.

Industry/Entity Type

Real Estate

Font styles to use
Sans Serif

Colors

Designer to choose colors to be used in the design.

Requirements
Must have
• navigation:
1)Home 2) Auction Calendar 3) Real Estate Listings 4) Services 5) About Us 6) Contact Us

Client mentions liking the http://www.tevorbidhouse.com site. Site will have no 'swooshes' as this will be developed on a responsive theme. Designs will needs to reflect this. Site will have slideshow - perhaps in the header of the site. Use stock real estate photo for initial image.

Home page will feature the text below and and auction list (as seen in tevorbidhouse.com). Widgets will include:
1) social icons (Chatterly, WorkLoop and RSS )
2) testimonials widget
3) featured auctions widget
4) email signup form (name and email fields)

Footer will have the company logo, contact info, and affiliation logos (attached to project)

(homepage text)
Holt Real Estate & Auction Company is located in West Central Iowa in the county seat town of Marlow County, Marlow City, Iowa.

Dale R. Holt, Auctioneer/Realtor, is the current owner and has been active as the main Auctioneer and Broker since 1977. Dale is the fourth generation of Auctioneers serving the area since 1894.

Since 1894 and four generations of Auctioneers, Holt Real Estate & Auction Company has strived to offer honest and professional auction and real estate services.

We offer complete auction services, including Auctioneering, Clerking/Cashiering, and complete sale managment. Experienced in the auction sales of real estate, farms, farm machinery & equipment, estate and household sales, antique auctions, and business liquidations.

Our real estate agency handles the sales of residential, farm, recreational, and light commercial business properties and we have continued to be the #1 real estate firm in Marlow County for the past several years.

Member of the Federal Bidcallers Association, Prairie Bidcallers Association and the Allied Townships Board of Realtors.

Please feel free to contact us for more information about your auction and/or real estate needs.

```html
<!DOCTYPE html>
<html lang="en">
<head>
<meta charset="utf-8">
<title>Holt Real Estate &amp; Auction Co</title>
<link href="https://fonts.googleapis.com/css2?family=Raleway:wght@400;500;700&family=Arimo:ital,wght@0,400;0,700;1,400&display=swap" rel="stylesheet">
<style>
:root{
  --green:#1a5a26;
  --green-dark:#164a1f;
  --green-btn:#1f6b2b;
  --link-green:#2e9a3c;
  --ink:#222;
  --nav:#232323;
  --panel:#1b1b1b;
  --foot:#2a2a2a;
  --foot-bottom:#111;
  --card:#f1f1f1;
  --line:#cfcfcf;
}
*{margin:0;padding:0;box-sizing:border-box}
html,body{width:838px;height:1200px;overflow:hidden;background:#fff}
body{position:relative;font-family:Arimo,Arial,sans-serif;color:var(--ink)}
.abs{position:absolute}

/* header */
.brand{left:70px;top:14px;width:180px}
.brand-name{font-family:Raleway,sans-serif;font-weight:700;color:var(--green);font-size:40px;line-height:40px;letter-spacing:1px}
.brand-sub{font-family:Raleway,sans-serif;font-weight:700;color:var(--green);font-size:10px;line-height:13px}
.social{left:470px;top:32px;display:flex;align-items:center;gap:10px}
.social-label{font-family:Raleway,sans-serif;font-size:19px;color:#444;margin-right:4px}
.social-link{display:flex;align-items:center;gap:4px;font-size:11px;color:#333;text-decoration:none}
.social-link i{display:block;width:12px;height:12px;border-radius:2px}
.sq-chat{background:#2b4a9a}.sq-work{background:#1b7fbd}.sq-rss{background:#f29a1e}

/* nav */
.nav{left:0;top:96px;width:838px;height:36px;background:var(--nav);display:flex;align-items:center;padding-left:74px}
.nav a{color:#fff;text-decoration:none;font-size:12px;height:36px;display:flex;align-items:center;padding:0 25px;border-left:1px solid #3a3a3a}
.nav a:first-child{border-left:0}
.nav a.active{background:var(--green-btn);height:24px;padding:0 13px;border-radius:2px;margin-right:20px}

.hero{left:0;top:132px;width:838px;height:331px;background:linear-gradient(180deg,#2f4d2e 0%,#6f7f5c 30%,#55704a 60%,#3a5a2a 85%,#4d7a2e 100%)}

/* main */
.main{left:70px;top:490px;width:460px}
.main h1,.main h2{font-family:Raleway,sans-serif;font-weight:500;font-size:17px;text-transform:uppercase;color:#222}
.main h1{margin-bottom:13px}
.main p{font-size:10px;line-height:12.6px;margin-bottom:12.4px;padding-right:6px}
.main h2{margin-top:24px;margin-bottom:13px}

.auction{border:1px solid var(--line);background:var(--card);border-radius:3px;height:160px;padding:11px 12px;position:relative}
.auction h3{color:var(--green);font-size:11.5px;font-weight:700;text-transform:uppercase;margin-bottom:12px}
.auction-photo{position:absolute;left:13px;top:36px;width:126px;height:79px;border:2px solid #ccc;background:linear-gradient(180deg,#7fb6d8 0%,#9fb9a0 40%,#4a4a48 75%,#333 100%)}
.auction-info{position:absolute;left:148px;top:36px;width:290px;font-size:9.4px;line-height:12.5px}
.auction-info h4{color:var(--green);font-size:9.5px;font-weight:700;text-transform:uppercase;margin-bottom:3px}
.auction-info p{margin-bottom:7px}
.auction-info b{font-weight:700}
.auction-actions{position:absolute;left:18px;top:126px;display:flex;align-items:center;font-size:10.5px}
.auction-actions span{display:flex;align-items:center;gap:4px;padding-right:10px}
.auction-actions .gal{border-left:1px solid var(--line);padding-left:10px;padding-right:16px}
.bid-btn{background:var(--green-btn);color:#fff;font-weight:700;font-size:10px;padding:5px 9px;border-radius:3px}

.pager{left:140px;top:1036px;display:flex;align-items:center;gap:10px;font-size:7px;color:#333}
.pager b{display:flex;align-items:center;justify-content:center;width:15px;height:14px;background:#333;color:#fff;font-weight:400}

/* sidebar */
.widget{left:553px;width:215px;border-radius:3px;color:#fff}
.widget h3{font-family:Raleway,sans-serif;font-weight:500;font-size:19px;text-align:center;letter-spacing:.5px}
.w-email{top:481px;height:174px;background:var(--green-dark);padding:15px 15px 0 22px}
.w-email h3{margin-bottom:11px}
.field{height:24px;background:#fff;border:1px solid #ccc;color:#888;font-size:10px;padding:6px 6px;margin-bottom:17px;width:178px}
.subscribe{width:115px;height:26px;background:#0e0e0e;border-radius:4px;font-weight:700;font-size:11px;letter-spacing:.5px;display:flex;align-items:center;justify-content:center;margin:-2px 0 0 52px}
.w-feat{top:679px;height:212px;background:var(--panel);padding:10px 12px}
.w-feat h3{margin-bottom:6px}
.feat-photo{width:150px;height:69px;margin:0 auto 8px;border:2px solid var(--green);background:linear-gradient(180deg,#8fbde0 0%,#e8e4d8 45%,#b6a98e 80%,#5c7a45 100%)}
.feat-text{font-size:9.4px;line-height:11.4px;text-align:center;margin-bottom:10px;padding:0 12px}
.w-test{top:914px;height:174px;background:var(--panel);padding:10px 15px}
.w-test h3{margin-bottom:10px}
.quote{font-size:9.2px;line-height:13.8px;font-style:italic}
.q{font-family:Georgia,serif;font-size:15px;font-style:normal;line-height:0}
.author{text-align:right;color:var(--link-green);font-size:9.5px;font-style:italic;font-weight:700;text-decoration:underline;margin-top:8px}

/* footer */
.footer{left:0;top:1112px;width:838px;height:64px;background:var(--foot)}
.contact{left:78px;top:1125px;font-size:9.4px;line-height:15.5px;color:#cfcfcf}
.contact em{color:#ccc}
.badges{left:458px;top:1124px;display:flex;gap:8px;align-items:center}
.badge{background:#d8d8d8}
.foot-brand{left:628px;top:1122px;text-align:center;width:128px}
.foot-brand .brand-name{color:#e6e6e6;font-size:30px;line-height:30px}
.foot-brand .brand-sub{color:#e6e6e6;font-size:7px;line-height:9px}
.copy{left:0;top:1176px;width:838px;height:24px;background:var(--foot-bottom);color:#bbb;font-size:8.5px;font-style:italic;text-align:center;line-height:24px}
</style>
</head>
<body>

<header>
  <div class="abs brand">
    <div class="brand-name">HOLT</div>
    <div class="brand-sub">REAL ESTATE AND AUCTION CO</div>
    <div class="brand-sub">SINCE 1894</div>
  </div>
  <div class="abs social">
    <span class="social-label">Social Media:</span>
    <a class="social-link" href="#"><i class="sq-chat"></i>Chatterly</a>
    <a class="social-link" href="#"><i class="sq-work"></i>WorkLoop</a>
    <a class="social-link" href="#"><i class="sq-rss"></i>RSS</a>
  </div>
</header>

<nav class="abs nav">
  <a class="active" href="#">Home</a>
  <a href="#">Auction Calendar</a>
  <a href="#">Real Estate Listings</a>
  <a href="#">Services</a>
  <a href="#">About Us</a>
  <a href="#">Contact Us</a>
</nav>

<div class="abs hero" role="img" aria-label="Slideshow photo of a green two-storey family home with dormers and a front porch, surrounded by trees and flower beds"></div>

<main class="abs main">
  <h1>Welcome to Holt Real Estate...</h1>
  <p>Holt Real Estate &amp; Auction Company is located in West Central Iowa in the county seat town of Marlow County, Marlow City, Iowa.</p>
  <p>Dale R. Holt, Auctioneer/Realtor, is the current owner and has been active as the main Auctioneer and Broker since 1977. Dale is the fourth generation of Auctioneers serving the area since 1894.</p>
  <p>Since 1894 and four generations of Auctioneers, Holt Real Estate &amp; Auction Company has strived to offer honest and professional auction and real estate services.</p>
  <p>We offer complete auction services, including Auctioneering, Clerking/Cashiering, and complete sale managment. Experienced in the auction sales of real estate, farms, farm machinery &amp; equipment, estate and household sales, antique auctions, and business liquidations.</p>
  <p>Our real estate agency handles the sales of residential, farm, recreational, and light commercial business properties and we have continued to be the #1 real estate firm in Marlow County for the past several years.</p>
  <p>Member of the Federal Bidcallers Association, Prairie Bidcallers Association and the Allied Townships Board of Realtors.</p>
  <p>Please feel free to contact us for more information about your auction and/or real estate needs.</p>

  <h2>Upcoming Auctions</h2>
  <article class="auction">
    <h3>Absolute Online Only Auction – Antiques &amp; Collectibles</h3>
    <div class="auction-photo" role="img" aria-label="Photo of a crowd gathered outside a house at a live auction"></div>
    <div class="auction-info">
      <h4>Live On-Site Auction</h4>
      <p>Vossberg BS3F High Lift, 600 Series Corvane tractor w/Hollis Loader, Dune buggy, 1207 RV Cutditioner: SHOP &amp;</p>
      <p><b>Begins:</b>&nbsp; Saturday, March 16, 2013 at 10:00 AM EDT</p>
      <p><b>Location:</b>&nbsp; 5312 Alder Road Linwood, KY 40118</p>
    </div>
    <div class="auction-actions">
      <span><svg width="10" height="10" viewBox="0 0 10 10"><circle cx="4" cy="4" r="3" fill="none" stroke="#222" stroke-width="1.6"/><path d="M6.2 6.2 9.3 9.3" stroke="#222" stroke-width="1.8"/></svg>Details</span>
      <span class="gal"><svg width="14" height="10" viewBox="0 0 14 10"><rect x=".5" y=".5" width="13" height="9" fill="none" stroke="#222"/><path d="M2 8 5 4 8 7 10 5 12 8Z" fill="#222"/></svg>Gallery</span>
      <span class="bid-btn">Click here for our online Bidding site</span>
    </div>
  </article>
</main>

<div class="abs pager">
  <span>‹‹ Previous</span><b>1</b><b>2</b><b>3</b><b>4</b><b>5</b><b>6</b><b>7</b><b>8</b><span>Next ››</span>
</div>

<aside>
  <section class="abs widget w-email">
    <h3>Email Sign up</h3>
    <div class="field">Your Name</div>
    <div class="field">Your Email</div>
    <div class="subscribe">SUBSCRIBE</div>
  </section>
  <section class="abs widget w-feat">
    <h3>Featured Auction</h3>
    <div class="feat-photo" role="img" aria-label="Photo of a white estate home with palm trees"></div>
    <p class="feat-text"><b>AUCTION!!!</b> - 5127±sf, 5+ Bedroom / 6.5 Bath Estate Home w/ Pool on 2.28± acres</p>
    <p class="feat-text">Tuesday <b>April 23</b>, 2013 at 10:00 AM<br>Cedar Pond 48 Cedar Pond Rd<br><b>Lake Harmon, FL 33921</b></p>
  </section>
  <section class="abs widget w-test">
    <h3>ClientTestimonials</h3>
    <p class="quote"><span class="q">“</span> Lorem Ipsum has been the industry's standard dummy text ever since the 1500s, when an unknown printer took a galley of type and scrambled it to make a type speci men book.It has survived not only five centuries, <span class="q">”</span></p>
    <p class="author">Ansel Moreno</p>
  </section>
</aside>

<footer>
  <div class="abs footer"></div>
  <div class="abs contact">
    <em>Holt Real Estate &amp; Auction Co- Since 1894</em><br>
    418 3rd Avenue NW • Pine Hollow, FL 33812<br>
    Phone : 555-214-7390 &nbsp; Fax: 555-214-7391 &nbsp; info@holtrealestate.com
  </div>
  <div class="abs badges" aria-label="Affiliations">
    <div class="badge" style="width:30px;height:30px;border-radius:50%"></div>
    <div class="badge" style="width:30px;height:30px"></div>
    <div class="badge" style="width:30px;height:30px"></div>
  </div>
  <div class="abs foot-brand">
    <div class="brand-name">HOLT</div>
    <div class="brand-sub">REAL ESTATE AND AUCTION CO</div>
    <div class="brand-sub">SINCE 1894</div>
  </div>
  <div class="abs copy">Copyright © 2008 - 2013 • Holt Real Estate &amp; Auction Co- • All Rights Reserved.</div>
</footer>

</body>
</html>
```